Easy Marinade Labels for Butchery Store

Need a set of labels designed for a Butchery Shop. They will sit in the top left corner of the packets as a triangle (7cm each side). Easy because the only major requirement is the label name and some small text saying "Please ask in store to see spec sheet for ingredients". Extra points for finding a fun way to incorporate the logo and/or images of food (garlic bulbs, chilli, spices ect) to enhance the label. List of Marinade Names below: GarlicPepper Mint & RosemarySatayBBQChilli Plum & GingerSundried Tomato & BasilBuffaloHoney SoyHoi-SinPer PeriSpicy CajunTeriyakiBlack Bean Ive also attached the logo and an example of how the label might sit on a packet of meat. Thanks

Target Market(s)

Butchery Deli Shop Customers

Industry/Entity Type

Food Store

Font styles to use
Serif
Sans Serif
Decorative
Other font styles liked:
• Fun font that isn't a generic Quillbrenn Font?

Colors

Designer to choose colors to be used in the design.

Requirements
Must have
• Product Name
• Small text saying "Please ask in store to see spec sheet for ingredients"
Nice to have
• Photos of ingredients that would match that type of marinade - Chilli, Garlic, Spices.
• Tavo Crest Logo - not essential if it doesn't look good on the label / doesn't fit.

```html
<!DOCTYPE html>
<html lang="en">
<head>
<meta charset="utf-8">
<title>Satay Marinade Label</title>
<link rel="stylesheet" href="https://fonts.googleapis.com/css2?family=Permanent+Marker&family=Oswald:wght@700&display=swap">
<style>
  :root {
    --paper: #ffffff;
    --frame-yellow: #ece524;
    --label-text: #ffffff;
    --lime: #a9cf3a;
    --leaf: #3f8a3c;
    --peanut: #d7a874;
    --chilli: #b8322a;
    --garlic: #e9e3e2;
  }
  * { margin: 0; padding: 0; box-sizing: border-box; }
  html, body {
    width: 1200px;
    height: 900px;
    overflow: hidden;
    background: var(--paper);
  }
  .canvas {
    position: relative;
    width: 1200px;
    height: 900px;
    background: var(--paper);
  }
  .label-shape {
    position: absolute;
    left: 0;
    top: 0;
    width: 1200px;
    height: 900px;
  }
  .marinade-name {
    position: absolute;
    left: 0;
    width: 1248px;
    top: 405px;
    text-align: center;
    font-family: "Permanent Marker", cursive;
    font-size: 150px;
    line-height: 1;
    color: var(--label-text);
    transform: translateX(-24px) rotate(-2deg);
    letter-spacing: 2px;
  }
  .ingredients-note {
    position: absolute;
    left: 250px;
    width: 748px;
    top: 598px;
    text-align: center;
    font-family: "Oswald", sans-serif;
    font-weight: 700;
    font-size: 24px;
    line-height: 1;
    letter-spacing: 2.6px;
    color: var(--label-text);
    text-transform: uppercase;
    white-space: nowrap;
  }
</style>
</head>
<body>
<main class="canvas">
  <svg class="label-shape" viewBox="0 0 1200 900" xmlns="http://www.w3.org/2000/svg">
    <defs>
      <clipPath id="label-clip">
        <polygon points="623,178 151,646 1096,646"/>
      </clipPath>
      <linearGradient id="ingredient-tones" x1="0" y1="0" x2="1" y2="0">
        <stop offset="0" stop-color="var(--leaf)"/>
        <stop offset="0.3" stop-color="var(--leaf)"/>
        <stop offset="0.45" stop-color="var(--peanut)"/>
        <stop offset="0.65" stop-color="var(--peanut)"/>
        <stop offset="0.78" stop-color="var(--lime)"/>
        <stop offset="1" stop-color="var(--lime)"/>
      </linearGradient>
      <radialGradient id="chilli-glow" cx="0.5" cy="0.38" r="0.3">
        <stop offset="0" stop-color="var(--chilli)" stop-opacity="0.55"/>
        <stop offset="1" stop-color="var(--chilli)" stop-opacity="0"/>
      </radialGradient>
      <linearGradient id="garlic-top" x1="0" y1="0" x2="0" y2="1">
        <stop offset="0" stop-color="var(--garlic)"/>
        <stop offset="0.3" stop-color="var(--garlic)" stop-opacity="0.6"/>
        <stop offset="0.5" stop-color="var(--garlic)" stop-opacity="0"/>
      </linearGradient>
    </defs>
    <g class="ingredient-photo" clip-path="url(#label-clip)" role="img"
       aria-label="Photo collage of satay ingredients: garlic cloves, dried red chillies, basil leaves, ginger root, kaffir lime leaves and a halved lime">
      <rect x="140" y="170" width="970" height="480" fill="url(#ingredient-tones)"/>
      <rect x="140" y="170" width="970" height="480" fill="url(#chilli-glow)"/>
      <rect x="140" y="170" width="970" height="480" fill="url(#garlic-top)"/>
    </g>
    <polygon class="label-frame" points="623,175 146,648 1102,648"
             fill="none" stroke="var(--frame-yellow)" stroke-width="6.5" stroke-linejoin="miter"/>
  </svg>
  <h1 class="marinade-name">SATAY</h1>
  <p class="ingredients-note">Please ask in store to see spec sheet for ingredients</p>
</main>
</body>
</html>
```